goal design

We are rolling out a goal for the next 3 years. the goal is as follows:
2014: $8 million gross profit, $1.25 million net income
2015: $12 million gross profit, $2.4 million net income
2016 $15 million gross profit, $4 million net income
We want a design that captures these numbers and that we can publish company wide that will quickly remind everyone of these goals. Our website is www.brookvalerecruiting.example. This will be an internal campaign. We will use the simple design to remind our people of our goals for the next 3 years. We will print it on mouse pads, shirts and things of this nature periodically to keep it front of mind for our people. So easy to remember, visually appealing and simple are good guidelines.
Updates
Target Market(s)
This is an internal campaign. it is to remind our people of our goals for the next few years so will be on little reminder items (i.e. cell phone covers, mouse pads, shirts, screen savers, etc).
Industry/Entity Type
It Company
Look and feel

```html
<!DOCTYPE html>
<html lang="en">
<head>
<meta charset="utf-8">
<title>Three-Year Goals 2014–2016</title>
<link rel="stylesheet" href="https://fonts.googleapis.com/css2?family=Anton&family=Roboto+Condensed:ital,wght@0,700;1,400&display=swap">
<style>
  :root {
    --bg-light: #fcdc3c;
    --bg-dark: #fd9410;
    --teal: #2fb6bb;
    --lime: #e5ff17;
    --shadow-orange: #d9661c;
    --magenta: #b8108f;
    --grid-grey: #e4e8e8;
  }
  html, body {
    margin: 0;
    padding: 0;
    overflow: hidden;
  }
  .canvas {
    position: relative;
    width: 1200px;
    height: 1000px;
    overflow: hidden;
    background: linear-gradient(160deg, var(--bg-light) 0%, #fcc52a 55%, var(--bg-dark) 100%);
    font-family: "Anton", "Roboto Condensed", sans-serif;
  }
  .goal-illustration {
    position: absolute;
    left: 412px;
    top: 150px;
    width: 340px;
    height: 270px;
    border-radius: 12px 12px 0 0;
    background: linear-gradient(180deg, var(--magenta) 0%, var(--magenta) 29%, var(--grid-grey) 29%, #ffffff 100%);
    box-shadow: 8px 8px 0 var(--shadow-orange);
  }
  .year-banner {
    position: absolute;
    left: 122px;
    top: 440px;
    width: 952px;
    height: 190px;
    transform: rotate(-5.4deg);
    transform-origin: left top;
    background: var(--teal);
    border: 9px solid var(--lime);
    border-radius: 26px;
    box-shadow: 10px 10px 0 var(--shadow-orange);
    display: flex;
    justify-content: space-between;
    align-items: center;
    padding: 0 34px;
    box-sizing: border-box;
  }
  .year {
    color: var(--lime);
    font-family: "Anton", sans-serif;
    font-size: 138px;
    line-height: 1;
    letter-spacing: 1px;
    margin-top: 2px;
  }
  .goal-card {
    position: absolute;
    width: 212px;
    height: 238px;
    background: var(--lime);
    border-radius: 8px;
    box-shadow: 9px 9px 0 var(--shadow-orange);
    transform: rotate(-2.5deg);
    box-sizing: border-box;
    padding: 32px 20px 0 12px;
    text-align: right;
    color: var(--teal);
  }
  .goal-card--2014 { left: 170px; top: 612px; }
  .goal-card--2015 { left: 488px; top: 576px; }
  .goal-card--2016 { left: 809px; top: 540px; padding-top: 28px; }
  .metric { margin-bottom: 22px; }
  .metric__value {
    font-family: "Roboto Condensed", sans-serif;
    font-weight: 700;
    font-size: 44px;
    line-height: 1;
    letter-spacing: -1px;
  }
  .metric__label {
    font-family: "Roboto Condensed", sans-serif;
    font-style: italic;
    font-weight: 400;
    font-size: 22px;
    line-height: 1.1;
  }
</style>
</head>
<body>
<main class="canvas">
  <div class="goal-illustration" role="img" aria-label="Illustration of a calendar with a bullseye target hit by a dart"></div>

  <section class="year-banner" aria-label="Goal years">
    <span class="year">2014</span>
    <span class="year">2015</span>
    <span class="year">2016</span>
  </section>

  <article class="goal-card goal-card--2014">
    <div class="metric">
      <div class="metric__value">8,000,000</div>
      <div class="metric__label">gross profit</div>
    </div>
    <div class="metric">
      <div class="metric__value">1,250,000</div>
      <div class="metric__label">net income</div>
    </div>
  </article>

  <article class="goal-card goal-card--2015">
    <div class="metric">
      <div class="metric__value">12,000,000</div>
      <div class="metric__label">gross profit</div>
    </div>
    <div class="metric">
      <div class="metric__value">2,400,000</div>
      <div class="metric__label">net income</div>
    </div>
  </article>

  <article class="goal-card goal-card--2016">
    <div class="metric">
      <div class="metric__value">15,000,000</div>
      <div class="metric__label">gross profit</div>
    </div>
    <div class="metric">
      <div class="metric__value">4,000,000</div>
      <div class="metric__label">net income</div>
    </div>
  </article>
</main>
</body>
</html>
```